Wordpress Design Project (Brookmere)

We need a wordpress design for an established auction and real estate company based in New Hampshire. The winning design will incorporate the colors of logo (red and blue) creatively with black or gray in a very professional and clean layout. Client mentions liking the site http://www.tarvellauction.com/ as a general idea.

Industry/Entity Type

Real Estate

Requirements
Must have
• Navigation:
1) Home (lorem text)
2) Upcoming Auctions
3) Auction Results
4) Sell or Consign
5) About Us
6) Services
7) FAQ
8) Contact Us

Site will have slideshow, initial image attached.
Sidebar widgets:
- Email sign up form
- Featured Auction (like at http://www.pinderauctionco.com) - - - - Video Widget
- Testimonials widget

Footer will have smaller logo, contact info, and 2 association logos (attached)
-
Nice to have
• use of drop-down menu design for 'Services'
1) Appraisals
2) Consulting
Should not have
• please use no gavels in the design

```html
<!DOCTYPE html>
<html lang="en">
<head>
<meta charset="utf-8">
<title>Brookmere Auctions</title>
<link href="https://fonts.googleapis.com/css2?family=Josefin+Sans:wght@300;400&family=Montserrat:wght@400;600;700&family=Open+Sans:wght@300;400&display=swap" rel="stylesheet">
<style>
:root{
  --navy:#101a4e;
  --red:#c8060a;
  --red-dark:#9e0a0c;
  --grey:#cfcfcf;
  --text:#555;
  --white:#fff;
}
*{box-sizing:border-box;margin:0;padding:0}
html,body{width:723px;height:1200px;overflow:hidden}
body{position:relative;background:var(--white);font-family:"Open Sans",sans-serif;color:var(--text)}
.abs{position:absolute}

/* header */
.brand{left:62px;top:12px;display:flex;align-items:center;gap:10px}
.brand-mark{width:56px;height:56px;border-radius:50%;background:var(--navy)}
.brand-name{font-family:"Montserrat",sans-serif;font-weight:600;font-size:22px;color:var(--navy);letter-spacing:.5px}
.social{left:578px;top:10px;display:flex;gap:4px}
.social span{width:18px;height:18px;border-radius:50%;display:block}
.search{left:512px;top:40px;width:150px;height:26px;display:flex}
.search-field{flex:1;background:#ececec;font-size:13px;color:#aaa;padding:3px 8px}
.search-btn{width:25px;background:var(--red-dark);display:flex;align-items:center;justify-content:center}

.nav-item{position:absolute;top:96px;font-family:"Josefin Sans",sans-serif;font-size:8.2px;line-height:10px;color:#555;white-space:nowrap;text-decoration:none}
.nav-item.active{font-family:"Montserrat",sans-serif;font-weight:700;font-size:8px;color:var(--navy)}
.nav-item.active::after,.nav-item.open::after{content:"";position:absolute;left:-2px;right:-2px;top:12px;height:5px;background:var(--red-dark)}
.nav-rule{left:0;top:112px;width:723px;height:3px;background:var(--navy)}

/* hero */
.hero{left:0;top:115px;width:723px;height:323px;overflow:hidden}
.hero-photo{position:absolute;inset:0;background:linear-gradient(90deg,#6b5a4c 0%,#8d7a66 25%,#5c4c40 45%,#1b1f4a 60%,#0f1550 100%)}
.hero-swirl{position:absolute;left:440px;top:20px;width:330px;height:300px;border-radius:50%;background:radial-gradient(circle at 55% 45%,#0f1550 30%,#a8101c 32%,#a8101c 55%,rgba(168,16,28,0) 58%)}
.hero-copy{position:absolute;right:60px;top:186px;text-align:right;color:var(--white)}
.hero-copy .l1{font-family:"Montserrat",sans-serif;font-weight:700;font-size:46px;line-height:50px;letter-spacing:1px}
.hero-copy .l2{font-family:"Josefin Sans",sans-serif;font-weight:300;font-size:38px;line-height:42px}
.hero-copy .l3{font-family:"Open Sans",sans-serif;font-size:22.5px;line-height:30px}
.hero-arrow{position:absolute;width:24px;height:24px;border:1.5px solid var(--white);transform:rotate(45deg)}
.dropdown{left:498px;top:116px;width:114px;background:rgba(20,26,80,.85);font-size:9px;color:var(--white)}
.dropdown div{padding:5px 10px;border-bottom:1px solid rgba(200,6,10,.6)}

.pager{left:0;top:438px;width:723px;height:37px;background:linear-gradient(#f2f2f2,#d8d8d8);display:flex;justify-content:center;align-items:center;gap:5px}
.pager span{width:13px;height:13px;border-radius:50%;background:var(--navy);border:1px solid var(--navy)}
.pager .off{background:var(--white)}

/* content */
.welcome{left:60px;top:494px}
.welcome .w1{font-family:"Josefin Sans",sans-serif;font-weight:300;font-size:38px;line-height:40px;color:var(--navy)}
.welcome .w2{font-family:"Montserrat",sans-serif;font-weight:700;font-size:44px;line-height:48px;color:var(--red-dark)}
.intro{left:62px;top:584px;width:382px;font-size:8.4px;line-height:11px;color:#666}
.intro p{margin-bottom:6px}
.section-title{left:60px;top:730px;display:flex;align-items:center;gap:4px;font-family:"Montserrat",sans-serif;font-weight:600;font-size:21px;color:var(--navy)}
.section-title i{width:30px;height:30px;border-radius:50%;background:var(--red-dark);display:block}
.quote{left:84px;top:770px;width:350px;font-size:11.5px;line-height:15px;color:#444}
.video{left:82px;top:807px;width:357px;height:202px;border:2px solid #888;background:linear-gradient(#1b2233,#3a3f48 60%,#252930)}
.video-bar{left:82px;top:1008px;width:357px;height:37px;background:var(--red);display:flex;align-items:center;padding-left:12px;color:var(--white);font-family:"Josefin Sans",sans-serif;font-size:13px}
.video-bar .plus{width:16px;height:16px;border:1px solid var(--white);transform:rotate(45deg);margin-right:12px}
.video-dots{position:absolute;right:12px;top:14px;display:flex;gap:3px}
.video-dots span{width:9px;height:9px;background:var(--white)}
.video-dots .on{background:var(--navy)}

/* sidebar */
.sidebar{left:469px;top:475px;width:194px;height:572px;background:var(--grey)}
.widget-title{left:469px;width:194px;text-align:center;color:var(--navy)}
.mail-title{top:492px;font-family:"Josefin Sans",sans-serif;font-weight:300;font-size:16px}
.field{left:488px;width:155px;height:24px;background:var(--white);font-size:12px;color:#aaa;padding:4px 8px}
.subscribe{left:488px;top:594px;width:155px;height:24px;background:var(--red);color:var(--white);text-align:center;font-family:"Josefin Sans",sans-serif;font-weight:300;font-size:14px;line-height:25px}
.up1{top:641px;font-family:"Josefin Sans",sans-serif;font-size:13px}
.up2{top:653px;font-family:"Montserrat",sans-serif;font-weight:700;font-size:26px}
.auction-img{left:491px;top:700px;width:148px;height:96px;border:2px solid var(--red);background:linear-gradient(#7c6b5d,#3d3340)}
.readmore{left:593px;top:781px;font-size:8px;color:#ddd}
.auction-info{left:469px;top:801px;width:194px;text-align:center;font-size:7.5px;line-height:10px;color:#444}
.cl1{top:845px;font-family:"Montserrat",sans-serif;font-weight:700;font-size:16px}
.cl2{top:865px;font-family:"Josefin Sans",sans-serif;font-size:12px}
.testimonial{left:475px;top:884px;width:168px;height:156px;background:var(--white);border:1px solid #bbb}
.t-photo{left:483px;top:895px;width:54px;height:66px;background:linear-gradient(#d9b58f,#b4846a)}
.t-name{left:540px;top:900px;font-family:"Montserrat",sans-serif;font-weight:600;font-size:10.5px;color:var(--navy)}
.t-lead{left:544px;top:918px;width:94px;font-size:7.6px;line-height:10px;color:#555}
.t-body{left:481px;top:965px;width:152px;font-size:7.6px;line-height:10px;color:#555}
.t-time{left:585px;top:1020px;font-size:8px;color:#555}
.scrollbar{left:647px;top:884px;width:14px;height:156px;background:var(--red);border:1px solid #bbb}
.scroll-thumb{left:649px;top:896px;width:10px;height:34px;background:var(--white);border:1px solid #bbb}

/* footer */
.footer-rule{left:0;top:1105px;width:723px;height:3px;background:var(--navy)}
.badge-a{left:70px;top:1135px;width:30px;height:28px;background:#888;border-radius:3px}
.badge-b{left:123px;top:1136px;width:102px;height:24px;background:#111}
.copyright{left:68px;top:1174px;font-size:8.5px;color:#444}
.footer-brand{left:486px;top:1122px;display:flex;align-items:center;gap:8px}
.footer-brand .brand-mark{width:50px;height:50px}
.footer-brand .brand-name{font-size:19px}
.phone{left:553px;top:1164px;display:flex;align-items:center;gap:3px;font-family:"Montserrat",sans-serif;font-size:16px;color:var(--red)}
</style>
</head>
<body>

<header>
  <div class="abs brand"><span class="brand-mark"></span><span class="brand-name">BROOKMERE</span></div>
  <div class="abs social" aria-label="Social links">
    <span style="background:var(--red)"></span><span style="background:#3a9ad9"></span><span style="background:#2b5db0"></span><span style="background:#e8701a"></span>
  </div>
  <div class="abs search">
    <div class="search-field">search</div>
    <div class="search-btn"><svg width="14" height="14" viewBox="0 0 14 14"><circle cx="6" cy="6" r="4.2" fill="none" stroke="#fff" stroke-width="2"/><line x1="9" y1="9" x2="13" y2="13" stroke="#fff" stroke-width="2.2"/></svg></div>
  </div>
  <nav>
    <a class="nav-item active" style="left:63px">HOME</a>
    <a class="nav-item" style="left:116px">UPCOMING AUCTIONS</a>
    <a class="nav-item" style="left:233px">AUCTION RESULTS</a>
    <a class="nav-item" style="left:332px">SELL OR CONSIGN</a>
    <a class="nav-item" style="left:433px">ABOUT US</a>
    <a class="nav-item open" style="left:499px">SERVICES</a>
    <a class="nav-item" style="left:564px">FAQ</a>
    <a class="nav-item" style="left:607px">CONTACT US</a>
  </nav>
  <div class="abs nav-rule"></div>
</header>

<section class="abs hero">
  <div class="hero-photo" role="img" aria-label="Crowd at a benefit auction raising numbered bidding paddles"></div>
  <div class="hero-swirl" role="img" aria-label="Large red brand decoration on navy"></div>
  <div class="hero-arrow" style="left:73px;top:153px"></div>
  <div class="hero-arrow" style="left:627px;top:137px"></div>
  <div class="hero-copy">
    <div class="l1">MAXIMIZE</div>
    <div class="l2">YOUR FUNDRAISING FOR</div>
    <div class="l3">Record Breaking Benefit Auctions</div>
  </div>
</section>
<div class="abs dropdown"><div>Appraisals</div><div>Consulting</div></div>

<div class="abs pager"><span></span><span class="off"></span><span></span><span></span></div>

<main>
  <div class="abs welcome"><div class="w1">Welcome to</div><div class="w2">BROOKMERE</div></div>
  <div class="abs intro">
    <p>Lorem ipsum dolor sit amet, consectetuer adipiscing elit, sed diam nonummy nibh euismod tincidunt ut laoreet dolore magna aliquam erat volutpat. Ut wisi enim ad minim veniam, quis nostrud exerci tation ullamcorper suscipit lobortis nisl ut aliquip ex ea commodo consequat. Duis autem vel eum iriure dolor in hendrerit in vulputate velit esse molestie consequat, vel illum dolore eu feugiat nulla facilisis at vero eros et accumsan et iusto odio dignissim qui blandit praesent luptatum zzril delenit augue duis dolore te feugait nulla facilisi.</p>
    <p>Diam nonummy nibh euismod tincidunt laoreet dolore magna aliquam erat volutpat. Ut wisi enim ad minim veniam, quis nostrud exerci tation ullamcorper suscipit lobortis nisl ut aliquip ex ea commodo consequat. Duis autem vel eum iriure dolor in hendrerit in vulputate velit esse molestie consequat, vel illum dolore eu feugiat nulla facilisis at vero eros et accumsan et iusto odio dignissim qui blandit praesent luptatum zzril delenit augue duis dolore te feugait nulla facilisi.</p>
  </div>
  <div class="abs section-title"><i></i>VIDEOS</div>
  <p class="abs quote">“Quis nostrud exerci tation ullamcorper suscipit lobortis nisl ut aliquip ex ea commodo consequat”</p>
  <div class="abs video" role="img" aria-label="Video still of a modern building beside a sculpture at dusk">
    <svg style="position:absolute;left:150px;top:75px" width="54" height="54" viewBox="0 0 54 54"><circle cx="27" cy="27" r="24" fill="none" stroke="#fff" stroke-width="3"/><polygon points="21,15 39,27 21,39" fill="#fff"/></svg>
  </div>
  <div class="abs video-bar"><span class="plus"></span>More Videos
    <div class="video-dots"><span></span><span class="on"></span><span></span><span></span></div>
  </div>
</main>

<aside>
  <div class="abs sidebar"></div>
  <div class="abs widget-title mail-title">Join Our Mailing List</div>
  <div class="abs field" style="top:524px">Name</div>
  <div class="abs field" style="top:558px">E-mail</div>
  <div class="abs subscribe">Subscribe</div>
  <div class="abs widget-title up1">UPCOMING</div>
  <div class="abs widget-title up2">AUCTIONS</div>
  <div class="abs auction-img" role="img" aria-label="Audience bidding at a live auction"></div>
  <div class="abs readmore">Readmore</div>
  <div class="abs auction-info">04/10/13 at 11:00 AM EDT<br>418 Orchard Rd.<br>Dover, NH 03820</div>
  <div class="abs widget-title cl1">OUR CLIENTS</div>
  <div class="abs widget-title cl2">SAY ABOUT US</div>
  <div class="abs testimonial"></div>
  <div class="abs t-photo" role="img" aria-label="Portrait of the client"></div>
  <div class="abs t-name">Dana Whitfield</div>
  <p class="abs t-lead">“ Diam nonummy nibh euismod tincidunt laoreet dolore magna aliquam erat volutpat.</p>
  <p class="abs t-body">Ut wisi enim ad minim veniam, quis nostrud exerci tation ullamcorper suscipit lobortis nisl ut aliquip ex ea commodo consequat.”</p>
  <div class="abs t-time">2 hours ago</div>
  <div class="abs scrollbar"></div>
  <div class="abs scroll-thumb"></div>
</aside>

<footer>
  <div class="abs footer-rule"></div>
  <div class="abs badge-a" aria-label="Association badge"></div>
  <div class="abs badge-b" aria-label="Association badge"></div>
  <p class="abs copyright">Copyright © Brookmere 2013 All rights reserved.</p>
  <div class="abs footer-brand"><span class="brand-mark"></span><span class="brand-name">BROOKMERE</span></div>
  <div class="abs phone"><svg width="14" height="14" viewBox="0 0 14 14"><path d="M3 1l3 3-1.5 2a8 8 0 0 0 3.5 3.5L10 8l3 3-2 2C6 13 1 8 1 3z" fill="var(--red)"/></svg>00 00 47 00</div>
</footer>

</body>
</html>
```